Hearth Table Cover Design

Open to creative ideas, we don't have a set cover style in mind so have fun with it!
Front Cover for Ebook-Quorvex and vantor shelf. Book title is "Hearth Table" sub title is "A Gentle Map for Kitchen Rhythms", Author is Corinne L Waddell. Website is www.theolwynkitchenworks.com.
Open to creative ideas, we dont' have a set cover style in mind so have fun with it!
We have attached some pictures of Corinne which could be incorporated into the title. We can send you high def files if you need.
We have attached two book covers which we like to get you started, but feel free to have fun, we're looking for something creative and catchy

```html
<!DOCTYPE html>
<html lang="en">
<head>
<meta charset="utf-8">
<title>Hearth Table — Cover</title>
<link rel="stylesheet" href="https://fonts.googleapis.com/css2?family=Bodoni+Moda:opsz,wght@6..96,400;6..96,500;6..96,700&display=swap">
<style>
  :root {
    --ink: #111111;
    --teal: #1d6676;
    --teal-soft: #2f8193;
    --white: #ffffff;
    --photo-light: #f4f2ee;
    --photo-mid: #e6dcc6;
    --photo-warm: #cdb48c;
    --photo-green: #3f8a5c;
    --photo-skin: #e9c2a6;
  }
  * { margin: 0; padding: 0; box-sizing: border-box; }
  html, body {
    width: 900px;
    height: 1200px;
    overflow: hidden;
    background: var(--white);
  }
  .cover {
    position: relative;
    width: 900px;
    height: 1200px;
    overflow: hidden;
    font-family: "Bodoni Moda", "Didot", serif;
  }
  .cover-photo {
    position: absolute;
    inset: 0;
    background:
      radial-gradient(ellipse 360px 520px at 230px 330px, var(--photo-skin) 0%, rgba(233,194,166,0.55) 40%, rgba(233,194,166,0) 75%),
      radial-gradient(ellipse 380px 420px at 260px 900px, var(--photo-green) 0%, rgba(63,138,92,0.6) 45%, rgba(63,138,92,0) 80%),
      radial-gradient(ellipse 300px 600px at 140px 500px, var(--photo-warm) 0%, rgba(205,180,140,0) 80%),
      linear-gradient(90deg, var(--photo-mid) 0%, var(--photo-light) 55%, #f8f8f6 100%);
  }
  .title {
    position: absolute;
    right: 54px;
    top: 150px;
    text-align: right;
    font-weight: 700;
    font-size: 84px;
    line-height: 70px;
    letter-spacing: 1px;
  }
  .title-line-1 { display: block; color: var(--ink); }
  .title-line-2 { display: block; color: var(--teal); }
  .subtitle {
    position: absolute;
    right: 68px;
    top: 384px;
    text-align: right;
    color: var(--teal-soft);
    font-weight: 400;
    font-size: 30px;
    line-height: 51px;
    letter-spacing: 1px;
  }
  .byline {
    position: absolute;
    left: 158px;
    top: 940px;
    color: var(--ink);
    font-weight: 500;
    font-size: 45px;
    line-height: 1;
    letter-spacing: 1px;
  }
  .author {
    position: absolute;
    left: 120px;
    top: 1005px;
    color: var(--ink);
    font-weight: 400;
    font-size: 70px;
    line-height: 1;
    white-space: nowrap;
  }
  .website {
    position: absolute;
    left: 0;
    width: 900px;
    top: 1088px;
    padding-left: 0;
    text-align: center;
    color: var(--white);
    font-weight: 500;
    font-size: 29px;
    line-height: 1;
    letter-spacing: 1px;
    transform: translateX(-5px);
  }
</style>
</head>
<body>
  <main class="cover">
    <div class="cover-photo" role="img" aria-label="Portrait photograph of the author, smiling, with long wavy blonde hair and a green t-shirt, standing against a softly blurred light street background"></div>

    <h1 class="title">
      <span class="title-line-1">hearth</span>
      <span class="title-line-2">table</span>
    </h1>

    <p class="subtitle">a gentle map for<br>kitchen rhythms</p>

    <p class="byline">written by</p>
    <p class="author">Corinne L Waddell</p>

    <p class="website">theolwynkitchenworks.com</p>
  </main>
</body>
</html>
```